Dune Air & Plus business card

I need an awesome, double-sided business card designed with our new logo. I would like the one side black with the colored logo, and the back side is all yours. I'd like to see horizontal and vertical layouts. Get creative! Thank you.

Target Market(s)

HVAC, Heating and Cooling in Phoenix, AZ

Industry/Entity Type

HVAC

Contact Information for Business Card

We need our new logo on the card. Tom Harker, (623) 555-0142, tom@trydunesair.com, www.trydunesair.com, ROC 514273

```html
<!DOCTYPE html>
<html lang="en">
<head>
<meta charset="utf-8">
<title>Dune Air &amp; Plus – Business Card</title>
<link href="https://fonts.googleapis.com/css2?family=Fira+Sans:wght@500;600;700;800&display=swap" rel="stylesheet">
<style>
  :root {
    --backdrop: #e4e4e4;
    --card: #222222;
    --text-light: #ffffff;
    --brand-blue: #1f80d8;
    --brand-orange: #f28a1e;
    --pill-start: #e0322b;
    --pill-end: #f7a531;
    --ghost: #353535;
  }
  * { margin: 0; padding: 0; box-sizing: border-box; }
  html, body {
    width: 1010px;
    height: 1200px;
    overflow: hidden;
    background: var(--backdrop);
    font-family: "Fira Sans", Arial, sans-serif;
  }
  .canvas {
    position: relative;
    width: 1010px;
    height: 1200px;
  }
  .card {
    position: absolute;
    left: 70px;
    width: 867px;
    height: 496px;
    background: var(--card);
    overflow: hidden;
  }
  .card--front { top: 63px; }
  .card--back { top: 633px; }

  .brand-lockup {
    position: absolute;
    inset: 0;
    display: flex;
    align-items: center;
    justify-content: center;
    gap: 22px;
  }
  .brand-lockup__dot {
    width: 38px;
    height: 38px;
    border-radius: 50%;
    background: var(--brand-orange);
  }
  .brand-lockup__name {
    color: var(--brand-blue);
    font-weight: 800;
    font-size: 78px;
    letter-spacing: 1px;
  }

  .ghost-name {
    position: absolute;
    right: 40px;
    top: 150px;
    color: var(--ghost);
    font-weight: 800;
    font-size: 72px;
    line-height: 1.05;
    text-align: right;
    white-space: nowrap;
  }
  .ghost-name span { display: block; }

  .contact {
    position: absolute;
    left: 52px;
    top: 100px;
    color: var(--text-light);
  }
  .contact__licence {
    margin-left: 110px;
    font-weight: 600;
    font-size: 25px;
    letter-spacing: 1px;
  }
  .contact__name {
    margin-left: 32px;
    margin-top: 2px;
    font-weight: 700;
    font-size: 58px;
    line-height: 1.1;
  }
  .contact__phone {
    display: inline-block;
    margin-top: 14px;
    width: 420px;
    height: 53px;
    padding-left: 48px;
    border-radius: 12px;
    background: linear-gradient(90deg, var(--pill-start), var(--pill-end));
    font-weight: 500;
    font-size: 34px;
    line-height: 53px;
    letter-spacing: 1px;
  }
  .contact__links {
    margin-top: 58px;
    margin-left: 55px;
    font-weight: 600;
    font-size: 25px;
    line-height: 40px;
  }
</style>
</head>
<body>
<main class="canvas">
  <section class="card card--front" aria-label="Card front">
    <div class="brand-lockup">
      <span class="brand-lockup__dot"></span>
      <span class="brand-lockup__name">Dune Air &amp; Plus</span>
    </div>
  </section>

  <section class="card card--back" aria-label="Card back">
    <p class="ghost-name" aria-hidden="true"><span>Dune Air</span><span>&amp; Plus</span></p>
    <div class="contact">
      <p class="contact__licence">ROC 514273</p>
      <p class="contact__name">Tom Harker</p>
      <p class="contact__phone">(623) 555-0142</p>
      <div class="contact__links">
        <p>tom@trydunesair.com</p>
        <p>www.trydunesair.com</p>
      </div>
    </div>
  </section>
</main>
</body>
</html>
```